Website Landing Page for Brightfall Systems

Create a custom designed website landing page for our business. Looking for a professional upscale design that incorporates our logo and logo colors into the theme. I want a standard fixed frame website, not a constant scrolling format that seems to be the trend. To start with I'm looking for more of the graphic design part, maybe a concept or theme, I don't expect to see a finished project. Not interested in generic templates or layouts.

The name of our company is Brightfall Systems and I've attached our logo below. I'd like to have the web page have the same look and feel of our logo, as well as the colors. Our company, Brightfall Systems does system design, installation, and programming, of residential and commercial Audio/Video and Automation systems. We do home theaters, lighting and building automation, video conferencing systems, security camera installations, conference rooms, projectors, distributed audio systems, and similar Technology projects. This will be a professional services/informational website. We will not sell products on this website. This website will be used to advertise our company and communicate our services to prospective customers. Having a well designed, professional and clean website is one way we want to distinguish our company from the competition.

Here are some examples of what I consider a professional well designed website
http://www.qorlamstudio.com/Work/

Last year we had our tradlo store designed (with PixelMarket) and I'm really happy with the way it turned out. You can see it at www.HolvenGearDepot.com I consider this to be a great design and looking for the same level of quality with this new website. However, do not copy or use any part of this design in this new project. This tradlo store is completely separate from our other company Brightfall Systems. I only mention this tradlo store an an example of good work.

Reason: Still going through designs.

Reason: Still working on project and have not had time to review all designs and request revisions.

Reason: Sill going through designs and requesting revisions

Reason: still going through all the submissions we received.

Target Market(s)

People interested in Audio/Video, home theaters, home automation. We do sales, system design, and programming. We typically work on larger projects with both residential and commercial customers.

Industry/Entity Type

Business

Number of Pages Required

1 page

Requirements
Must have
• Great design elements. Please use a white background. I think white goes well with our logo colors.

```html
<!DOCTYPE html>
<html lang="en">
<head>
<meta charset="utf-8">
<title>Brightfall Systems</title>
<link rel="stylesheet" href="https://fonts.googleapis.com/css2?family=Lato:wght@300;400;700&display=swap">
<style>
  :root {
    --white: #ffffff;
    --ink: #5b6459;
    --nav-ink: #4e5a5f;
    --body-ink: #6d7479;
    --brand-blue: #3a9dd6;
    --band-blue: #8fd0ec;
    --accent-green: #4cb848;
    --dot-active: #0bb5ee;
    --dot-idle: #83d7f4;
    --ring-grey: #eceef0;
    --hero-navy: #2a3f6b;
  }
  * { box-sizing: border-box; margin: 0; padding: 0; }
  html, body { width: 1093px; height: 1200px; overflow: hidden; background: var(--white); }
  body { position: relative; font-family: "Lato", sans-serif; }

  .hero { position: absolute; left: 0; top: 0; width: 1093px; height: 600px; overflow: hidden; }
  .hero-photo { position: absolute; }
  .photo-building { left: 0; top: 0; width: 358px; height: 286px; background: linear-gradient(160deg, #3d5a8c, #1f3358 70%, #2c4a7a); }
  .photo-home { left: 0; top: 286px; width: 358px; height: 314px; background: linear-gradient(180deg, #4a4235, #7a6a55 55%, #5c4f40); }
  .photo-tower { left: 360px; top: 0; width: 368px; height: 600px; background: linear-gradient(200deg, #3b5687, #24375e 50%, #31496f); }
  .photo-conference { left: 728px; top: 0; width: 365px; height: 297px; background: linear-gradient(170deg, #5f646b, #2f3d52 60%, #3a4555); }
  .photo-video { left: 728px; top: 297px; width: 365px; height: 303px; background: linear-gradient(180deg, #6a4a3e, #4a3a36 50%, #7d7f82); }

  .hero-lines { position: absolute; left: 0; top: 0; }

  .service-label {
    position: absolute; display: flex; align-items: center; justify-content: center;
    border: 3px solid var(--white); color: var(--white); text-align: center;
    font-size: 42px; line-height: 1.12; font-weight: 400;
    text-shadow: 0 1px 3px rgba(0,0,0,.35);
  }
  .label-building { left: 60px; top: 70px; width: 266px; height: 126px; }
  .label-conference { left: 772px; top: 66px; width: 266px; height: 129px; }
  .label-home { left: 60px; top: 380px; width: 266px; height: 130px; }
  .label-video { left: 770px; top: 357px; width: 267px; height: 158px; }

  .hero-badge {
    position: absolute; left: 460px; top: 198px; width: 174px; height: 174px; border-radius: 50%;
    background: var(--white); display: flex; align-items: center; justify-content: center;
    color: var(--brand-blue); font-weight: 700; font-size: 22px; text-align: center; line-height: 1.15;
  }

  .site-header { position: absolute; left: 0; top: 600px; width: 1093px; height: 110px; }
  .brand { position: absolute; left: 112px; top: 614px; display: flex; align-items: center; gap: 12px; }
  .brand-dot { width: 54px; height: 54px; border-radius: 50%; border: 4px solid var(--brand-blue); }
  .brand-name { color: var(--brand-blue); font-weight: 700; font-size: 17px; line-height: 1.1; letter-spacing: .5px; text-transform: uppercase; }

  .main-nav { position: absolute; top: 622px; left: 482px; display: flex; }
  .main-nav a { display: block; color: var(--nav-ink); text-decoration: none; font-size: 23px; font-weight: 400; height: 52px; padding: 0 0 0 0; margin-right: 48px; position: relative; }
  .main-nav a:last-child { margin-right: 0; }
  .main-nav a.is-current { width: 104px; text-align: center; margin-right: 30px; }
  .main-nav a.is-current::after { content: ""; position: absolute; left: 0; right: 0; bottom: 0; height: 8px; background: var(--accent-green); }

  .content { position: absolute; left: 0; top: 690px; width: 1093px; height: 510px; }

  .section-title { position: absolute; left: 0; top: 736px; width: 1093px; text-align: center; color: var(--ink); font-size: 38px; font-weight: 700; }

  .feature-photo {
    position: absolute; left: 198px; top: 855px; width: 286px; height: 200px; border-radius: 8px;
    background: linear-gradient(180deg, #8a7a5e, #d9d2c3 45%, #8c7a62);
  }

  .feature-card {
    position: absolute; left: 546px; top: 818px; width: 390px; height: 274px; background: var(--white);
    border-radius: 10px; box-shadow: 0 2px 14px rgba(0,0,0,.08);
  }
  .card-title { position: absolute; left: 0; top: 16px; width: 100%; text-align: center; color: var(--ink); font-size: 24px; font-weight: 400; }
  .card-rule { position: absolute; left: 155px; width: 80px; height: 4px; background: var(--accent-green); }
  .card-rule.top { top: 56px; }
  .card-rule.bottom { top: 250px; }
  .card-side { position: absolute; top: 110px; width: 4px; height: 72px; background: var(--brand-blue); }
  .card-side.left { left: 18px; }
  .card-side.right { left: 376px; }
  .card-text { position: absolute; left: 46px; top: 90px; width: 307px; color: var(--body-ink); font-size: 19.5px; font-weight: 300; line-height: 24.5px; text-align: justify; text-align-last: center; }

  .slider-dots { position: absolute; top: 1118px; left: 483px; display: flex; align-items: center; gap: 20px; }
  .slider-dots span { width: 18px; height: 18px; border-radius: 50%; background: var(--dot-idle); }
  .slider-dots span.is-active { width: 27px; height: 27px; background: var(--dot-active); }
</style>
</head>
<body>

<section class="hero">
  <div class="hero-photo photo-building" role="img" aria-label="Glass office building facade under blue sky"></div>
  <div class="hero-photo photo-home" role="img" aria-label="Living room with home theater screen and sofa"></div>
  <div class="hero-photo photo-tower" role="img" aria-label="Tall glass skyscraper viewed from below"></div>
  <div class="hero-photo photo-conference" role="img" aria-label="Auditorium style conference room with rows of seats"></div>
  <div class="hero-photo photo-video" role="img" aria-label="Boardroom with table and wood panelled wall"></div>

  <svg class="hero-lines" width="1093" height="600" viewBox="0 0 1093 600" aria-hidden="true">
    <g fill="none" stroke="#ffffff" stroke-width="3">
      <polyline points="326,70 482,228"/>
      <polyline points="772,68 725,68 725,216 602,216"/>
      <polyline points="326,508 360,508 360,358 500,358"/>
      <polyline points="607,348 770,512"/>
    </g>
  </svg>

  <div class="service-label label-building">Building<br>Automation</div>
  <div class="service-label label-conference">Conference<br>Rooms</div>
  <div class="service-label label-home">Home<br>Automation</div>
  <div class="service-label label-video">Video<br>Conferencing<br>Systems</div>

  <div class="hero-badge">Brightfall<br>Systems</div>
</section>

<svg class="content" width="1093" height="510" viewBox="0 690 1093 510" aria-hidden="true">
  <g fill="none" stroke="var(--ring-grey)" stroke-width="3">
    <circle cx="57" cy="757" r="41"/>
    <circle cx="233" cy="777" r="60"/>
    <circle cx="610" cy="770" r="80"/>
    <circle cx="808" cy="855" r="68"/>
    <circle cx="1000" cy="778" r="83"/>
    <circle cx="90" cy="912" r="72"/>
    <circle cx="1110" cy="1000" r="120"/>
    <circle cx="215" cy="1095" r="108"/>
    <circle cx="30" cy="1108" r="50"/>
    <circle cx="420" cy="1100" r="55"/>
    <circle cx="585" cy="1120" r="80"/>
    <circle cx="880" cy="1150" r="80"/>
    <circle cx="1040" cy="1190" r="40"/>
  </g>
  <g fill="none" stroke="var(--brand-blue)" stroke-width="5">
    <rect x="194" y="828" width="325" height="231" rx="10"/>
    <rect x="162" y="851" width="325" height="231" rx="10"/>
  </g>
</svg>

<svg class="site-header" width="1093" height="110" viewBox="0 600 1093 110" aria-hidden="true">
  <defs>
    <filter id="band-shadow" x="-5%" y="-50%" width="110%" height="300%">
      <feDropShadow dx="0" dy="3" stdDeviation="5" flood-color="#000" flood-opacity=".08"/>
    </filter>
  </defs>
  <rect x="0" y="600" width="1093" height="75" fill="#ffffff" filter="url(#band-shadow)"/>
  <rect x="0" y="675" width="1093" height="12" fill="var(--band-blue)"/>
  <path d="M100 675 A36 36 0 0 0 170 675 Z" fill="var(--band-blue)"/>
  <path d="M106 681 A30 30 0 0 0 164 681" fill="#ffffff"/>
</svg>

<div class="brand">
  <span class="brand-dot"></span>
  <span class="brand-name">Brightfall<br>Systems</span>
</div>

<nav class="main-nav">
  <a href="#" class="is-current">Home</a>
  <a href="#">Services</a>
  <a href="#">Customers</a>
  <a href="#">Contact us</a>
</nav>

<h1 class="section-title">Lorem ipsum dolor sit amet</h1>

<div class="feature-photo" role="img" aria-label="Home theater living room with wall screen and sofa"></div>

<article class="feature-card">
  <h2 class="card-title">Lorem ipsum</h2>
  <span class="card-rule top"></span>
  <span class="card-side left"></span>
  <span class="card-side right"></span>
  <p class="card-text">Lorem ipsum dolor sit amet, con&shy;sectetuer adipiscing elit. Aenean commodo ligula eget dolor. Aenean massa. Cum sociis natoque penati&shy;bus et magnis dis parturient montes, nascetur ridiculus mus.</p>
  <span class="card-rule bottom"></span>
</article>

<div class="slider-dots">
  <span class="is-active"></span>
  <span></span>
  <span></span>
  <span></span>
</div>

</body>
</html>
```